Advertisement insert for magazine

Create a 5 X 4.75 advertisement for a magazine. Design must catch the eye of the reader and properly represent our brand. This will be in LANTERN magazine a local affluent magazine.

The goal of this advertisement is to represent a progressive firm with an amazing portfolio.

Target Market(s)

local businesses and business leaders of Florida.

Industry/Entity Type

Architecture

Font styles to use
Other font styles liked:
• Calibri, Calibri light

Requirements
Must have
• Modern Progressive Design. Our logo, our address and telephone number and our project images we have attached.
Should not have
• I have attached the ad from last year, we DO NOT want to replicate this ad, however this should give you an idea of the size and overall goal of the advertisement.
• (SEE LANTERN MAGAZINE KTW PDF)

```html
<!DOCTYPE html>
<html lang="en">
<head>
<meta charset="utf-8">
<title>Marlowe Reyes + Partners — Architecture · Interior Design</title>
<link rel="stylesheet" href="https://fonts.googleapis.com/css2?family=Montserrat:wght@400;500&family=Roboto+Condensed:wght@300&display=swap">
<style>
  :root {
    --navy: #1b2a4b;
    --navy-deep: #14203b;
    --frame: #f3f2f6;
    --banner: #0b0b0d;
    --accent: #1f7ccf;
    --paper: #f2f1f6;
    --ink-grey: #6f7075;
    --name-grey: #8d8e92;
  }
  * { margin: 0; padding: 0; box-sizing: border-box; }
  html, body { width: 1200px; height: 1146px; overflow: hidden; background: var(--paper); }
  .ad { position: relative; width: 1200px; height: 1146px; background: var(--paper); font-family: "Montserrat", sans-serif; }
  .portfolio-field {
    position: absolute; left: 0; top: 0; width: 1200px; height: 888px;
    background: radial-gradient(ellipse at 85% 10%, #24365c 0%, transparent 45%),
                radial-gradient(ellipse at 10% 60%, #22335a 0%, transparent 50%),
                linear-gradient(160deg, var(--navy) 0%, var(--navy-deep) 100%);
  }
  .photo-frame { position: absolute; background: var(--frame); }
  .photo { position: absolute; }
  .frame-feature { left: 79px; top: 47px; width: 1040px; height: 528px; }
  .frame-feature .photo { left: 18px; top: 18px; right: 18px; bottom: 18px;
    background: linear-gradient(180deg, #dfe9f2 0%, #9cc3d9 30%, #6a9bc1 55%, #2e4f93 70%, #c9a97c 88%, #e8e4dc 100%); }
  .frame-small { top: 590px; width: 332px; height: 243px; }
  .frame-small .photo { left: 22px; top: 18px; right: 22px; bottom: 18px; }
  .frame-lounge { left: 79px; }
  .frame-lounge .photo { background: linear-gradient(180deg, #e6e6e4 0%, #9aa39c 35%, #6a6a6c 65%, #d8d2c8 100%); }
  .frame-lobby { left: 433px; }
  .frame-lobby .photo { background: linear-gradient(180deg, #5b6a3a 0%, #b58a5a 40%, #9a4a2c 70%, #6b3a22 100%); }
  .frame-stair { left: 788px; }
  .frame-stair .photo { background: linear-gradient(120deg, #f4f3f1 0%, #dcdad6 50%, #eae8e4 70%, #3a3a3a 100%); }
  .discipline-banner {
    position: absolute; left: 75px; top: 860px; width: 832px; height: 58px;
    background: var(--banner); clip-path: polygon(10px 0, 100% 0, calc(100% - 10px) 100%, 0 100%);
    display: flex; align-items: center; padding-left: 39px;
    color: #fff; font-size: 32px; font-weight: 400; letter-spacing: 5.6px; white-space: nowrap;
  }
  .discipline-banner .divider { color: var(--accent); margin: 0 4px 0 0; font-size: 26px; }
  .brand { position: absolute; left: 72px; top: 950px; display: flex; align-items: center; gap: 24px; }
  .brand-dot { width: 110px; height: 110px; border-radius: 50%; background: var(--accent); flex: none; }
  .brand-name { font-size: 36px; font-weight: 500; color: var(--name-grey); letter-spacing: 0.5px; line-height: 1.1; }
  .contact { position: absolute; left: 680px; top: 968px; list-style: none;
    font-family: "Roboto Condensed", sans-serif; font-weight: 300; font-size: 24px; color: var(--ink-grey); }
  .contact li { display: flex; align-items: center; gap: 12px; height: 33px; white-space: nowrap; }
  .contact svg { width: 22px; height: 22px; flex: none; }
</style>
</head>
<body>
<main class="ad">
  <section class="portfolio-field">
    <figure class="photo-frame frame-feature">
      <div class="photo" role="img" aria-label="Poolside resort lounge with blue sofa, wicker chairs, striped umbrellas and palm trees"></div>
    </figure>
    <figure class="photo-frame frame-small frame-lounge">
      <div class="photo" role="img" aria-label="Office lounge with grey sectional sofa and round tables by tall windows"></div>
    </figure>
    <figure class="photo-frame frame-small frame-lobby">
      <div class="photo" role="img" aria-label="Warm lobby with terracotta tile floor, patterned sofa and potted palms"></div>
    </figure>
    <figure class="photo-frame frame-small frame-stair">
      <div class="photo" role="img" aria-label="Bright white atrium with glass-railed staircase and large black-and-white mural"></div>
    </figure>
  </section>

  <h2 class="discipline-banner">ARCHITECTURE<span class="divider">•</span>INTERIOR DESIGN</h2>

  <div class="brand">
    <span class="brand-dot"></span>
    <span class="brand-name">MARLOWE REYES<br>+ PARTNERS</span>
  </div>

  <ul class="contact">
    <li>
      <svg viewBox="0 0 24 24" aria-hidden="true"><path fill="var(--accent)" d="M6.6 10.8a15.1 15.1 0 0 0 6.6 6.6l2.2-2.2c.3-.3.7-.4 1-.2 1.1.4 2.3.6 3.6.6.6 0 1 .4 1 1V20c0 .6-.4 1-1 1A17 17 0 0 1 3 4c0-.6.4-1 1-1h3.5c.6 0 1 .4 1 1 0 1.3.2 2.5.6 3.6.1.3 0 .7-.2 1z"/></svg>
      (555) 014-2290
    </li>
    <li>
      <svg viewBox="0 0 24 24" aria-hidden="true" fill="none" stroke="var(--accent)" stroke-width="1.8"><circle cx="12" cy="12" r="9.5"/><ellipse cx="12" cy="12" rx="4" ry="9.5"/><path d="M2.5 12h19M4 7h16M4 17h16"/></svg>
      www.marlowereyes.com
    </li>
    <li>
      <svg viewBox="0 0 24 24" aria-hidden="true"><path fill="var(--accent)" d="M12 2a7 7 0 0 0-7 7c0 5.2 7 13 7 13s7-7.8 7-13a7 7 0 0 0-7-7zm0 9.5A2.5 2.5 0 1 1 12 6.5a2.5 2.5 0 0 1 0 5z"/></svg>
      418 Harbor Lane Coral Bay, FL 33000
    </li>
  </ul>
</main>
</body>
</html>
```